Website Design for two swimming school brands

Looking for a modern, engaging website design for my new business Every Stroke Water Learning. Within that business I have two current brands:
Every Stroke Swim and Yard Paddle
My current website (www.yardpaddle.net) has most of the info you'll need. Feel free to also use my socials for content.
Looking for someone to do the initial design/setup and then hand over full control to me with no ongoing fees or charges (except for hosting), and I'm responsible for all future changes. Ideally made and then can be edited in google sites but open to other options.

Website requirements are quite simple for both pages.
For the Yard Paddle page, I'd like the same info and features that are on my current website presented in a fresh way.
For the Every Stroke page, I'd like to see your concepts for design and possible sections, but it'll be roughly the same as the yard paddle one. I will upload a document soon for text and sections and other information to go on the Every stroke swim page.

For clarity the difference between the business' is one goes out to people's home pools and the other hires out lane space in public pool to conduct lessons.
I'd like a lighter theme for the Yard Paddle Website and a Darker one for the Every Stroke.
Both pages needs to be accessible with picture descriptions for screen reader and other similar features.

I currently use Bookora for all my inquiry, booking and payment functions so the website would need to be compatible with their widgets.

Have a look at the MockUp v2 or the business card design to get the concept of two different brandings working together.

Some text from the Every Stroke Swim Page can be found in this document:
https://files.examplecloud.net/doc/7QpLmZ2rTvXw9KcN4bYd/edit
-
Feel free to ask any further questions.

Target Market(s)

Families and disability service providers

Industry/Entity Type

Sports and Recreation

Coding

Coded - Design and coding required

Number of Pages Required

4 page

Requirements
Must have
• Engaging design, ability to put in widgets into website, cross links between two business
Nice to have
• Common elements across the two pages but also points of difference

```html
<!DOCTYPE html>
<html lang="en">
<head>
<meta charset="utf-8">
<title>Yard Paddle – Mobile Swimming Lessons</title>
<link rel="stylesheet" href="https://fonts.googleapis.com/css2?family=Lato:ital,wght@0,300;0,400;0,700;0,900;1,400&display=swap">
<style>
:root{
  --blue:#1a8fd0;
  --teal:#19a98e;
  --band:#deeef8;
  --ink:#333b44;
  --muted:#6b7178;
  --white:#ffffff;
}
*{box-sizing:border-box;margin:0;padding:0}
html,body{width:1200px;height:4556px;overflow:hidden}
body{position:relative;font-family:'Lato',sans-serif;color:var(--ink);background:var(--white)}
.abs{position:absolute}
/* top bar */
.topbar{left:0;top:0;width:1200px;height:35px;background:var(--blue);color:var(--white);font-size:11px;font-weight:900;letter-spacing:.3px}
.topbar .follow{left:113px;top:11px}
.social{top:6px;width:24px;height:24px;border-radius:50%;border:2px solid var(--white)}
.topbar .acc{top:11px}
.topbar .sep{top:0;width:1px;height:35px;background:rgba(255,255,255,.5)}
/* header */
.logo{font-weight:900;color:var(--teal);font-size:31px;letter-spacing:.5px;white-space:nowrap}
.contact-mini{font-size:13px;color:var(--ink);line-height:1.15}
.contact-mini small{display:block;font-size:9px;color:var(--blue);font-weight:700}
.mini-ico{width:22px;height:22px;border-radius:50%;background:var(--blue)}
.lang{left:998px;top:70px;width:89px;height:32px;border:1px solid #c9ced3;border-radius:3px;font-size:11px;font-weight:900;padding:9px 0 0 36px}
.lang i{position:absolute;left:14px;top:10px;width:14px;height:11px;background:#2a4aa0}
.nav a{position:absolute;top:126px;font-size:12px;font-weight:700;color:var(--ink);text-decoration:none;white-space:nowrap}
.nav a.on{color:var(--blue);border-bottom:2px solid var(--blue);padding-bottom:6px}
/* hero */
.hero{left:0;top:175px;width:1200px;height:613px;background:linear-gradient(160deg,#4f6a3a 0%,#7ea05a 25%,#3fa0c8 45%,#6cc2df 60%,#a07a52 80%,#7b5b3c 100%)}
.hero-arrow{top:290px;width:26px;height:40px}
.hero-badge{left:596px;top:250px;width:448px;height:448px;border-radius:50%;background:var(--white);border:8px solid var(--teal);display:flex;align-items:center;justify-content:center;text-align:center}
.hero-badge h1{font-size:37px;line-height:42px;font-weight:900;color:var(--teal);letter-spacing:.3px}
/* photos */
.photo{border-radius:6px;box-shadow:0 4px 12px rgba(0,0,0,.15)}
.section-title{width:1200px;left:0;text-align:center;font-size:39px;font-weight:300;color:var(--blue);letter-spacing:.5px}
.section-title b{font-weight:900}
.title-rule{left:570px;width:60px;height:2px;border-left:40px solid var(--blue);border-right:10px solid var(--blue);background:transparent}
.btn{display:flex;align-items:center;justify-content:center;font-size:12px;font-weight:900;color:var(--white);border-radius:3px}
.band{left:0;width:1200px;background:var(--band)}
.circle{border-radius:50%;background:var(--white);box-shadow:0 6px 18px rgba(0,0,0,.12);display:flex;flex-direction:column;align-items:center;justify-content:center;text-align:center}
.circle h3{font-weight:400;text-transform:uppercase}
.circle p{color:var(--muted)}
/* testimonials */
.avatar{border-radius:50%;background:linear-gradient(135deg,#5da8d8,#2c4e7a);border:3px solid var(--white);box-shadow:0 0 0 2px var(--teal)}
.card{left:311px;top:2294px;width:581px;height:180px;background:var(--white);box-shadow:0 3px 14px rgba(0,0,0,.15);text-align:center}
/* plans */
.price{font-size:21px;font-style:italic;line-height:34px;color:var(--muted);font-weight:400}
/* footer */
.fcol h4{font-size:15px;font-weight:900;color:var(--ink);margin-bottom:18px}
.fcol a{display:block;font-size:13px;color:var(--ink);text-decoration:none;margin-bottom:13px}
.fline{width:3px;height:40px;background:var(--teal)}
</style>
</head>
<body>

<!-- top bar -->
<div class="abs topbar">
  <span class="abs follow">FOLLOW US</span>
  <span class="abs social" style="left:200px"></span>
  <span class="abs social" style="left:234px"></span>
  <span class="abs social" style="left:268px"></span>
  <span class="abs social" style="left:302px"></span>
  <span class="abs acc" style="left:771px">MY ACCOUNT</span>
  <span class="abs sep" style="left:878px"></span>
  <span class="abs acc" style="left:897px">MESSAGE</span>
  <span class="abs sep" style="left:977px"></span>
  <span class="abs acc" style="left:1000px">ACCOUNT</span>
</div>

<!-- header -->
<div class="abs logo" style="left:99px;top:118px">YARD PADDLE</div>
<span class="abs mini-ico" style="left:636px;top:77px"></span>
<div class="abs contact-mini" style="left:665px;top:72px"><small>EMAIL US</small>info@yardpaddle.net</div>
<span class="abs mini-ico" style="left:818px;top:77px"></span>
<div class="abs contact-mini" style="left:848px;top:72px"><small>CALL US NOW</small>+61 400 555 018</div>
<div class="abs lang"><i></i>ENG ⌄</div>
<nav class="nav">
  <a class="on" style="left:424px">HOME</a>
  <a style="left:498px">ABOUT US</a>
  <a style="left:599px">SERVICES</a>
  <a style="left:694px">TESTIMONIALS</a>
  <a style="left:822px">PRICING</a>
  <a style="left:909px">PARTNERS</a>
  <a style="left:1011px">CONTACT US</a>
</nav>

<!-- hero -->
<div class="abs hero" role="img" aria-label="Backyard above-ground swimming pool with timber deck, flowering shrubs and planter boxes"></div>
<svg class="abs hero-arrow" style="left:52px;top:466px" viewBox="0 0 26 40"><path d="M20 4 6 20l14 16" stroke="#fff" stroke-width="4" fill="none"/></svg>
<svg class="abs hero-arrow" style="left:1118px;top:466px" viewBox="0 0 26 40"><path d="M6 4l14 16L6 36" stroke="#fff" stroke-width="4" fill="none"/></svg>
<div class="abs hero-badge"><h1>MOBILE SWIMMING<br>LESSONS FOR ALL<br>AGES AND ABILITIES<br>IN ADELAIDE</h1></div>

<!-- about -->
<div class="abs photo" style="left:113px;top:945px;width:205px;height:278px;background:linear-gradient(160deg,#8c6b4e,#c8a27a 50%,#5a4a3a)" role="img" aria-label="Swim instructor in a sun hat outdoors by a waterfall"></div>
<div class="abs photo" style="left:336px;top:898px;width:247px;height:240px;background:linear-gradient(180deg,#2aa4dc,#1c7fbf 60%,#9bd2ea)" role="img" aria-label="Instructor in the pool helping a swimmer at the steps"></div>
<div class="abs photo" style="left:330px;top:1163px;width:248px;height:162px;background:linear-gradient(135deg,#4fb6e6,#2b8cc8 55%,#caa08a)" role="img" aria-label="Smiling student in the water with her instructor"></div>
<h2 class="abs" style="left:645px;top:938px;font-size:39px;font-weight:300;color:var(--blue)"><b style="font-weight:900">ABOUT</b> US</h2>
<div class="abs" style="left:645px;top:981px;width:88px;height:2px;background:var(--blue)"></div>
<p class="abs" style="left:647px;top:999px;width:420px;font-size:14px;line-height:19.3px;color:var(--muted)">From a young age, teaching has come naturally to him and it is something that he truly enjoys. In his spare time, he enjoys hiking with friends and playing ultimate flying disc, including helping to coordinate a weekly social league. From a young age, teaching has come naturally to him and it is something that he truly enjoys. In his spare time, he enjoys hiking with friends and playing ultimate flying disc, including helping to coordinate a weekly social league. From a young age, teaching has come naturally to him and it is something that he truly enjoys. In his spare time, he enjoys hiking with friends and playing ultimate flying disc, including helping to coordinate.</p>
<div class="abs btn" style="left:647px;top:1246px;width:141px;height:42px;background:var(--teal)">LEARN MORE</div>

<!-- services -->
<div class="abs band" style="top:1449px;height:640px"></div>
<h2 class="abs section-title" style="top:1503px">OUR <b>SERVICES</b></h2>
<div class="abs title-rule" style="top:1557px"></div>
<div class="abs circle" style="left:99px;top:1645px;width:332px;height:332px;padding:0 46px">
  <h3 style="font-size:21px;line-height:29px;color:var(--ink)">Children and<br>teenagers</h3>
  <p style="font-size:12px;line-height:18px;margin:14px 0 10px">Jordan has over ten years of experience working with frightened four-year-olds right up to teenagers aspiring to club championships, he can help your child(ren) succeed.</p>
  <div class="btn" style="width:116px;height:32px;background:var(--blue);font-size:10px">LEARN MORE</div>
</div>
<div class="abs circle" style="left:800px;top:1648px;width:326px;height:326px;padding:0 48px">
  <h3 style="font-size:21px;color:var(--ink)">Adults</h3>
  <p style="font-size:12px;line-height:17px;margin:14px 0 10px">He works with people of all ages, backgrounds, and cultures. It doesn't matter if you have lived in Australia your whole life or have just arrived recently.</p>
  <div class="btn" style="width:112px;height:30px;background:var(--blue);font-size:10px">LEARN MORE</div>
</div>
<div class="abs circle" style="left:402px;top:1603px;width:416px;height:416px;background:var(--teal);padding:0 56px">
  <h3 style="font-size:26px;line-height:36px;color:var(--white)">Person with<br>disability</h3>
  <p style="font-size:16px;line-height:22px;color:var(--white);margin:16px 0 16px">The aquatic environment can provide freedom, comfort, and confidence to people with a disability. Jordan works with the individual adapting his approach and communication methods to meet their needs.</p>
  <div class="btn" style="width:144px;height:40px;background:var(--white);color:var(--teal)">LEARN MORE</div>
</div>

<!-- testimonials -->
<h2 class="abs section-title" style="top:2166px;color:var(--blue)"><b>TESTIMONIALS</b></h2>
<div class="abs title-rule" style="top:2220px"></div>
<div class="abs avatar" style="left:181px;top:2214px;width:26px;height:26px" role="img" aria-label="Client portrait"></div>
<div class="abs avatar" style="left:1033px;top:2226px;width:72px;height:72px" role="img" aria-label="Client portrait"></div>
<div class="abs avatar" style="left:-15px;top:2340px;width:72px;height:80px" role="img" aria-label="Client portrait"></div>
<div class="abs avatar" style="left:147px;top:2479px;width:60px;height:60px" role="img" aria-label="Client portrait"></div>
<div class="abs avatar" style="left:921px;top:2488px;width:42px;height:42px" role="img" aria-label="Client portrait"></div>
<div class="abs avatar" style="left:1178px;top:2512px;width:30px;height:30px" role="img" aria-label="Client portrait"></div>
<div class="abs card">
  <span class="abs" style="left:42px;top:14px;font-size:60px;font-weight:900;color:var(--blue);line-height:1">“</span>
  <p style="margin:52px auto 0;width:430px;font-size:13px;line-height:19px;font-style:italic;color:var(--muted)">Lorem ipsum dolor sit amet, consectetur adipiscing elit, sed do eiusmod tempor incididunt ut labore et dolore magna aliqua. Quis ipsum suspendisse ultrices gravida. Risus commodo viverra maecenas accumsan lacus vel facilisis.</p>
  <p style="margin-top:10px;font-size:13px"><span style="color:#f4b400;letter-spacing:3px">★★★★★</span> <span style="color:var(--blue);font-weight:700;margin-left:6px">Sep 09</span></p>
  <span class="abs" style="left:498px;top:100px;font-size:60px;font-weight:900;color:var(--blue);line-height:1">”</span>
</div>
<div class="abs avatar" style="left:562px;top:2249px;width:78px;height:78px" role="img" aria-label="Client portrait"></div>

<!-- plans -->
<div class="abs band" style="top:2651px;height:724px"></div>
<h2 class="abs section-title" style="top:2716px">OUR <b>PLANS</b></h2>
<div class="abs title-rule" style="top:2770px"></div>
<p class="abs" style="left:0;top:2788px;width:1200px;text-align:center;font-size:14px;font-style:italic;color:var(--muted)">$50 Off Peak - $57.50 Peak (Term 4 wk3 - End Term 4)</p>
<div class="abs circle" style="left:97px;top:2894px;width:326px;height:326px">
  <h3 style="font-size:28px;color:var(--ink);margin-bottom:10px">Extra time</h3>
  <p class="price">$15.00 (off peak)<br>$17.50 (peak)<br>per 15min<br>above 30 min</p>
  <p style="font-size:31px;font-weight:900;color:var(--teal);margin-top:10px">$15.00</p>
</div>
<div class="abs circle" style="left:800px;top:2894px;width:326px;height:326px">
  <h3 style="font-size:28px;line-height:40px;color:var(--ink);margin-bottom:8px">Lessons in<br>other pools</h3>
  <p class="price">$15.00 (off peak)<br>$17.50 (peak)<br>per 15min<br>above 30 min</p>
  <p style="font-size:31px;font-weight:900;color:var(--teal);margin-top:6px">$106.00</p>
</div>
<div class="abs circle" style="left:405px;top:2849px;width:416px;height:416px;background:var(--blue)">
  <h3 style="font-size:30px;line-height:46px;color:var(--white);margin-bottom:10px">Extra<br>swimmers free*</h3>
  <p class="price" style="color:var(--white);font-size:23px;line-height:38px">$15.00 (off peak)<br>$17.50 (peak)<br>per 15min<br>above 30 min</p>
  <p style="font-size:52px;font-weight:900;color:var(--white);margin-top:6px">$55.00</p>
</div>

<!-- links -->
<h2 class="abs section-title" style="top:3437px">OUR <b>LINKS</b></h2>
<div class="abs title-rule" style="top:3491px"></div>
<div class="abs" style="left:120px;top:3540px;width:186px;height:76px;border-radius:8px;background:#c9d7ea" role="img" aria-label="Partner badge"></div>
<div class="abs" style="left:375px;top:3548px;width:205px;height:60px;border-radius:8px;background:#c7d2ea" role="img" aria-label="Partner badge"></div>
<div class="abs" style="left:648px;top:3542px;width:175px;height:72px;border-radius:8px;background:#d9c9cf" role="img" aria-label="Partner badge"></div>
<div class="abs" style="left:925px;top:3542px;width:145px;height:72px;border-radius:8px;background:#d4d0e6" role="img" aria-label="Partner badge"></div>

<!-- contact -->
<div class="abs band" style="top:3693px;height:477px"></div>
<h2 class="abs section-title" style="top:3770px;color:var(--teal)">GET IN TOUCH <b style="color:var(--blue)">WITH US</b></h2>
<div class="abs title-rule" style="top:3824px"></div>
<div class="abs circle" style="left:245px;top:3870px;width:80px;height:80px">
  <svg width="28" height="36" viewBox="0 0 28 36"><path d="M14 0C6 0 0 6 0 14c0 10 14 22 14 22s14-12 14-22C28 6 22 0 14 0z" fill="var(--blue)"/><circle cx="14" cy="13" r="5" fill="#fff"/></svg>
</div>
<div class="abs circle" style="left:559px;top:3870px;width:80px;height:80px">
  <svg width="30" height="30" viewBox="0 0 24 24"><path d="M6.6 10.8a15.2 15.2 0 0 0 6.6 6.6l2.2-2.2a1 1 0 0 1 1-.25 11.4 11.4 0 0 0 3.6.57 1 1 0 0 1 1 1V20a1 1 0 0 1-1 1A17 17 0 0 1 3 4a1 1 0 0 1 1-1h3.5a1 1 0 0 1 1 1c0 1.25.2 2.45.57 3.57a1 1 0 0 1-.25 1z" fill="var(--blue)"/></svg>
</div>
<div class="abs circle" style="left:874px;top:3870px;width:80px;height:80px">
  <svg width="36" height="26" viewBox="0 0 36 26"><rect width="36" height="26" rx="3" fill="var(--blue)"/><path d="M2 3l16 12L34 3" stroke="#fff" stroke-width="2.5" fill="none"/></svg>
</div>
<div class="abs" style="left:135px;top:3974px;width:300px;text-align:center">
  <h3 style="font-size:23px;font-weight:400;color:var(--blue)">LOCATION</h3>
  <p style="font-size:13px;line-height:19px;color:var(--muted);margin-top:6px">We do the travelling to your<br>home or other pool that's<br>convenient to you</p>
</div>
<div class="abs" style="left:449px;top:3974px;width:300px;text-align:center">
  <h3 style="font-size:23px;font-weight:400;color:var(--blue)">AVAILABILITY</h3>
  <p style="font-size:13px;line-height:19px;color:var(--muted);margin-top:6px">We'll work with you to find a<br>time and day that is suitable</p>
</div>
<div class="abs" style="left:764px;top:3974px;width:300px;text-align:center">
  <h3 style="font-size:23px;font-weight:400;color:var(--blue)">EMAIL US</h3>
  <p style="font-size:13px;line-height:19px;color:var(--muted);margin-top:6px">Use the 'live site' icons on the<br>right or email us</p>
</div>

<!-- footer -->
<div class="abs logo" style="left:150px;top:4340px;font-size:28px">YARD PADDLE</div>
<span class="abs fline" style="left:410px;top:4268px"></span>
<div class="abs fcol" style="left:433px;top:4274px"><h4>NAVIGATION</h4><a>HOME</a><a>ABOUT US</a><a>SERVICES</a><a>PRICING</a><a>CONTACT</a></div>
<span class="abs fline" style="left:650px;top:4268px"></span>
<div class="abs fcol" style="left:666px;top:4274px"><h4 style="font-size:13px">RESOURCES</h4><a>OUR PARTNERS</a><a>TERMS &amp; CONDITIONS</a><a>PRIVACY POLICY</a></div>
<span class="abs fline" style="left:857px;top:4268px"></span>
<div class="abs fcol" style="left:885px;top:4276px"><h4 style="font-size:13px">CONTACT INFORMATION</h4></div>
<span class="abs mini-ico" style="left:885px;top:4306px;width:32px;height:32px"></span>
<p class="abs" style="left:930px;top:4305px;font-size:10px;line-height:13px;color:var(--muted)">42 RIDGEWAY LANE,<br>ADELAIDE SA 5000</p>
<span class="abs mini-ico" style="left:885px;top:4347px;width:32px;height:32px"></span>
<p class="abs" style="left:930px;top:4357px;font-size:11px;color:var(--muted)">+61 400 555 018</p>
<span class="abs mini-ico" style="left:885px;top:4389px;width:32px;height:32px"></span>
<p class="abs" style="left:930px;top:4399px;font-size:11px;color:var(--muted)">INFO@YARDPADDLE.NET</p>
<div class="abs" style="left:0;top:4485px;width:1200px;height:1px;background:#d6dadf"></div>
<p class="abs" style="left:0;top:4505px;width:1200px;text-align:center;font-size:11px;color:var(--muted)">© 2022 YARD PADDLE ALL RIGHT RESERVED</p>

</body>
</html>
```